Water Filtration Company needs a business card design using our existing logo/colours!

We design and manufacture and export specialised water filtration equipment. Our equipment will take unclean dirty water and filters to safe clean drinkable water.
We would like to see designs using our existing logo and colours (see attached "Palette") that represents clean safe drinking water (fresh, clean designs but still professional and modern). Our customers are other businesses who supply water filtration equipment, governments, and private individuals.
BUSINESS CARD DETAILS (Common details):
Tel: + 61 7 55 419 276
www: brindlepeak.com.au
Address: 3/47 Cordwell Parade
Marlow Flats NSW 2593 Australia
(please include the word Australia as we are an international company)
Must include: COMMERCIAL WATER FILTRATION EQUIPMENT
NAME NO 1:
Owen Pritch
General Manager
Mobile: +61 427 38 91 04
Email: owen@brindlepeak.com.au
NAME NO. 2:
Gina Rosk
Business Manager
Mobile: +61 409 572 148
Email: gina@brindlepeak.com.au
Must Have:
1) PRINT READY IN .AI & .PDF FORMATS
2) Also saved in file format .ai (Adobe Illustrator - compatible with CS4)
3) Use existing LOGO & COLOURS: Please use our logo (see attached file)
4) FONTS: we have used Avenir & Helvetica in the past but are open to other font types for the address etc.
Thank you!

```html
<!DOCTYPE html>
<html lang="en">
<head>
<meta charset="utf-8">
<title>Brindle Peak – Business Cards</title>
<link href="https://fonts.googleapis.com/css2?family=Nunito+Sans:wght@400;600;700&family=Oswald:wght@500;600&display=swap" rel="stylesheet">
<style>
  :root {
    --ink-blue: #0f5a84;
    --deep-blue: #0b4a70;
    --teal: #2aa7c2;
    --light-teal: #6fcddd;
    --paper: #ffffff;
    --stage: #e9ecef;
    --text-dark: #1f4f6e;
  }
  * { margin: 0; padding: 0; box-sizing: border-box; }
  html, body { width: 1200px; height: 1166px; overflow: hidden; }
  body {
    background: var(--stage);
    font-family: "Nunito Sans", Arial, sans-serif;
    position: relative;
  }
  .card {
    position: absolute;
    top: 434px;
    width: 520px;
    height: 297px;
    background: var(--paper);
    overflow: hidden;
    box-shadow: 0 6px 18px rgba(0,0,0,0.18);
  }
  .card--front { left: 60px; }
  .card--back { left: 620px; }
  .card__art { position: absolute; inset: 0; width: 100%; height: 100%; }

  .brand {
    position: absolute;
    display: flex;
    align-items: center;
    gap: 7px;
    color: var(--teal);
    font-weight: 700;
    white-space: nowrap;
    letter-spacing: -0.5px;
    line-height: 1;
  }
  .brand__dot {
    border-radius: 50%;
    background: var(--teal);
    flex: none;
  }
  .card--front .brand { left: 24px; top: 132px; font-size: 26px; }
  .card--front .brand__dot { width: 11px; height: 11px; }
  .card--back .brand { left: 70px; top: 112px; font-size: 58px; gap: 9px; }
  .card--back .brand__dot { width: 21px; height: 21px; }

  .contact {
    position: absolute;
    right: 24px;
    top: 26px;
    bottom: 22px;
    text-align: right;
    color: var(--paper);
    display: flex;
    flex-direction: column;
  }
  .contact__name {
    font-family: "Oswald", "Arial Narrow", sans-serif;
    font-weight: 600;
    font-size: 27px;
    line-height: 1;
    text-transform: uppercase;
  }
  .contact__role {
    font-family: "Oswald", "Arial Narrow", sans-serif;
    font-weight: 500;
    font-size: 11.5px;
    text-transform: uppercase;
    letter-spacing: 0.4px;
    margin-top: 3px;
  }
  .contact__address {
    font-size: 10.5px;
    line-height: 1.45;
    margin-top: 18px;
  }
  .contact__lines {
    margin-top: auto;
    list-style: none;
    font-size: 12px;
    line-height: 1.55;
  }
  .contact__lines li {
    display: flex;
    justify-content: flex-end;
    align-items: center;
    gap: 7px;
  }
  .icon { width: 11px; height: 11px; flex: none; }

  .tagline {
    position: absolute;
    left: 0;
    width: 430px;
    bottom: 16px;
    text-align: center;
    color: var(--ink-blue);
    font-weight: 700;
    font-size: 13px;
    text-transform: uppercase;
    letter-spacing: 0.2px;
  }
</style>
</head>
<body>

<section class="card card--front" aria-label="Business card front">
  <svg class="card__art" viewBox="0 0 520 297" preserveAspectRatio="none" aria-hidden="true">
    <path d="M236 0 C206 90 250 200 216 297 L520 297 L520 0 Z" fill="var(--ink-blue)"/>
    <path d="M226 0 C196 90 240 200 206 297" fill="none" stroke="var(--teal)" stroke-width="6"/>
    <path d="M221 0 C191 90 235 200 201 297" fill="none" stroke="var(--light-teal)" stroke-width="1.5"/>
  </svg>

  <div class="brand"><span class="brand__dot"></span>brindle peak</div>

  <div class="contact">
    <p class="contact__name">Owen Pritch</p>
    <p class="contact__role">General Manager</p>
    <p class="contact__address">3/47 Cordwell Parade<br>Marlow Flats NSW 2593 Australia</p>
    <ul class="contact__lines">
      <li>+61 427 38 91 04
        <svg class="icon" viewBox="0 0 12 12"><rect x="3" y="0.5" width="6" height="11" rx="1" fill="none" stroke="#fff"/><line x1="5" y1="9.5" x2="7" y2="9.5" stroke="#fff"/></svg>
      </li>
      <li>+ 61 7 55 419 276
        <svg class="icon" viewBox="0 0 12 12"><path d="M2 1 L4.5 1 L5.5 3.5 L4 4.7 C4.8 6.5 5.8 7.5 7.3 8.2 L8.5 6.7 L11 7.7 L11 10 C11 10.6 10.5 11 10 11 C5 10.5 1.5 7 1 2 C1 1.4 1.4 1 2 1 Z" fill="#fff"/></svg>
      </li>
      <li>owen@brindlepeak.com.au
        <svg class="icon" viewBox="0 0 12 12"><rect x="0.5" y="2.5" width="11" height="7.5" fill="#fff"/><path d="M0.5 2.5 L6 7 L11.5 2.5" fill="none" stroke="var(--ink-blue)"/></svg>
      </li>
      <li>www.brindlepeak.com.au
        <svg class="icon" viewBox="0 0 12 12"><circle cx="6" cy="6" r="5.3" fill="none" stroke="#fff"/><ellipse cx="6" cy="6" rx="2.3" ry="5.3" fill="none" stroke="#fff"/><line x1="0.7" y1="6" x2="11.3" y2="6" stroke="#fff"/></svg>
      </li>
    </ul>
  </div>
</section>

<section class="card card--back" aria-label="Business card back">
  <svg class="card__art" viewBox="0 0 520 297" preserveAspectRatio="none" aria-hidden="true">
    <path d="M520 20 C468 110 500 230 444 297 L520 297 Z" fill="var(--ink-blue)"/>
    <path d="M514 22 C462 112 494 232 436 297" fill="none" stroke="var(--teal)" stroke-width="5"/>
  </svg>

  <div class="brand"><span class="brand__dot"></span>brindle peak</div>

  <p class="tagline">Commercial Water Filtration Equipment</p>
</section>

</body>
</html>
```